Pine-Ridge Brokerage Business Cards

We have had success with our logo design and are looking to have a creative business card made. Logo must be prominent in the business card design. We would like headshots to be on the business card, but do not want the photo to be framed at all. We are looking for designs for two different people, so I will attach headshots

Target Market(s)

Home Buyers. Trying to market to younger/trendy crowd. 25-45 year of age.

Industry/Entity Type

Real Estate

Contact Information for Business Card

New business card design needed. Looking for a vibrant and attractive business card.

Font styles to use
Other font styles liked:
• Match the logo font on the Pine-Ridge QVT Realty logo

Requirements
Must have
• Must have sketch harbor logo incorporated. Fair Dwelling Logo should be very small and should be on the back of the card and is a requirement. Propvoy logo should be small and on the back of the card with FD logo.

2 different business cards, must have the following info:
Business card 1:
Dan Perrow & Marla Vinter
(555) 208-4417
Marla@prq.example
Marla.lakeviewhouselistings.example
2873 W Fernhill Rd, Brookvale, ZZ 00421

Business card 2:
Gregory Tamsell
(555) 394-1062
Greg@prq.example
Gregory.lakeviewhouselistings.example

```html
<!DOCTYPE html>
<html lang="en">
<head>
<meta charset="utf-8">
<title>Pine-Ridge QVT Realty – Business Card</title>
<link href="https://fonts.googleapis.com/css2?family=Montserrat:wght@500;700;800&family=Source+Sans+3:wght@400;600&display=swap" rel="stylesheet">
<style>
  :root {
    --navy: #0b2240;
    --orange: #f5a623;
    --sky: #6fc3ea;
    --cream: #fbe9c8;
    --paper: #ffffff;
    --stage: #e4e6e9;
    --ink: #0b2240;
    --muted: #1e2a3a;
  }
  * { box-sizing: border-box; margin: 0; padding: 0; }
  html, body { width: 1200px; height: 800px; overflow: hidden; }
  body {
    background: var(--stage);
    font-family: "Source Sans 3", "Helvetica Neue", Arial, sans-serif;
    position: relative;
  }
  .card {
    position: absolute;
    width: 580px;
    height: 331px;
    border-radius: 2px;
    overflow: hidden;
    box-shadow: 0 6px 18px rgba(0,0,0,.18);
  }

  /* Back side */
  .card--back { left: 560px; top: 40px; background: var(--navy); }
  .brand {
    display: flex; align-items: center; gap: 12px;
    font-family: "Montserrat", sans-serif;
    font-weight: 700;
    letter-spacing: .02em;
    white-space: nowrap;
  }
  .brand__dot { width: 18px; height: 18px; border-radius: 50%; background: var(--orange); flex: none; }
  .card--back .brand {
    position: absolute; left: 50%; top: 50%;
    transform: translate(-50%, -50%);
    color: var(--paper);
    font-size: 34px;
  }
  .card--back .brand__dot { width: 26px; height: 26px; }
  .badges { position: absolute; right: 26px; top: 24px; display: flex; gap: 12px; }
  .badge { width: 28px; height: 28px; border: 2px solid var(--paper); border-radius: 2px; }

  /* Front side */
  .card--front { left: 60px; top: 420px; background: var(--paper); }
  .headshot {
    position: absolute; right: 0; top: 0;
    width: 300px; height: 100%;
    background:
      radial-gradient(ellipse 60% 55% at 62% 62%, #cfccc6 0%, #d8d4cc 45%, rgba(216,212,204,0) 75%),
      linear-gradient(90deg, rgba(255,255,255,1) 0%, var(--cream) 30%, #f6ead6 100%);
  }
  .card--front .brand {
    position: absolute; left: 30px; top: 34px;
    color: var(--ink);
    font-size: 24px;
  }
  .agent { position: absolute; left: 30px; top: 104px; color: var(--ink); }
  .agent__name {
    font-family: "Montserrat", sans-serif;
    font-weight: 800;
    font-size: 19px;
    letter-spacing: .02em;
    text-transform: uppercase;
  }
  .agent__title { font-size: 14px; color: var(--muted); margin-top: 2px; }
  .contact { position: absolute; left: 30px; top: 172px; color: var(--muted); font-size: 15px; line-height: 1.45; }
  .contact__row { display: flex; align-items: center; gap: 14px; }
  .contact__item { display: inline-flex; align-items: center; gap: 5px; }
  .contact__item svg { flex: none; }
  .web-band {
    position: absolute; left: 0; bottom: 0;
    width: 330px; height: 40px;
    background: var(--navy);
    color: var(--paper);
    font-size: 15.5px;
    display: flex; align-items: center;
    padding-left: 24px;
  }
  .web-band__name { color: var(--orange); }
</style>
</head>
<body>

  <section class="card card--back" aria-label="Card back">
    <div class="brand"><span class="brand__dot"></span>Pine-Ridge QVT Realty</div>
    <div class="badges">
      <span class="badge" aria-label="Fair Dwelling badge"></span>
      <span class="badge" aria-label="Propvoy badge"></span>
    </div>
  </section>

  <section class="card card--front" aria-label="Card front">
    <div class="headshot" role="img" aria-label="Unframed headshot of Gregory Tamsell in a light grey quarter-zip, over a soft city skyline backdrop"></div>

    <div class="brand"><span class="brand__dot"></span>Pine-Ridge QVT Realty</div>

    <div class="agent">
      <div class="agent__name">Gregory Tamsell</div>
      <div class="agent__title">PROPVOY®</div>
    </div>

    <div class="contact">
      <div>2873 W Fernhill Rd, Brookvale, ZZ 00421</div>
      <div class="contact__row">
        <span class="contact__item">
          <svg width="12" height="12" viewBox="0 0 24 24" aria-hidden="true"><path fill="#f5a623" d="M6.6 10.8a15.1 15.1 0 0 0 6.6 6.6l2.2-2.2a1 1 0 0 1 1-.25 11.4 11.4 0 0 0 3.6.57 1 1 0 0 1 1 1V20a1 1 0 0 1-1 1A17 17 0 0 1 3 4a1 1 0 0 1 1-1h3.5a1 1 0 0 1 1 1c0 1.250.2 2.45.57 3.57a1 1 0 0 1-.25 1z"/></svg>
          (555) 394-1062
        </span>
        <span class="contact__item">
          <svg width="15" height="11" viewBox="0 0 20 14" aria-hidden="true"><rect x="1" y="1" width="18" height="12" fill="none" stroke="#f5a623" stroke-width="2"/><path d="M1 1l9 7 9-7" fill="none" stroke="#f5a623" stroke-width="2"/></svg>
          Greg@prq.example
        </span>
      </div>
    </div>

    <div class="web-band"><span class="web-band__name">Gregory</span>.lakeviewhouselistings.example</div>
  </section>

</body>
</html>
```